Mobile Tutoring Service needs a Flier for Distribution to Clients

Lantern Scholars Inc. is a tutoring company that uses video call technology to perform tutoring session in math, sciences, and standardized test preparation. We need a flier that we can distribute to email lists of parents in school districts around the St. Louis Area, as well as post in public areas to attract clients. The following file has the important information needed on the flier. In particular, the "How it Works" Steps 1-3 can be made into an animation or video that looks attractive and helps potential clients understand our process. Our logo is also found in the document. Ideally, all information in the power point slide will be in the flier.

Target Market(s)

Parents for middle and high schoolers grade 6-12 in the St. Louis Area

Industry/Entity Type

Tutoring

Font styles to use
Serif

Colors
3176b5
85abd2
0492cd
33a6d7
ceeaf5

Requirements
Must have
• All the information with the attached file
Nice to have
• A nice-looking animation instead of the still screen shoots that are included in the attached file.

```html
<!DOCTYPE html>
<html lang="en">
<head>
<meta charset="utf-8">
<title>Lantern Scholars – Mobile Tutoring Flier</title>
<link href="https://fonts.googleapis.com/css2?family=Roboto+Condensed:wght@400;700&display=swap" rel="stylesheet">
<style>
  :root {
    --brand-blue: #4a8ed0;
    --accent-blue: #5296d6;
    --deep-blue: #3176b5;
    --ink: #141414;
    --panel-dark: #0c0c0c;
    --footer-grey: #5f5f5f;
    --white: #ffffff;
    --page-bg: #ececec;
  }
  * { box-sizing: border-box; margin: 0; padding: 0; }
  html, body { width: 1200px; height: 1200px; overflow: hidden; }
  body {
    background: var(--page-bg);
    font-family: "Roboto Condensed", "Arial Narrow", sans-serif;
    position: relative;
  }
  .flier {
    position: absolute;
    left: 154px; top: 25px;
    width: 891px; height: 1150px;
    overflow: hidden;
    background: var(--panel-dark);
    color: var(--white);
  }
  .flier-backdrop { position: absolute; inset: 0; }
  .abs { position: absolute; }

  .brand-name {
    left: 44px; top: 198px;
    font-size: 33px; font-weight: 700; color: var(--ink);
    display: flex; align-items: center; gap: 10px;
    white-space: nowrap;
  }
  .brand-dot { width: 16px; height: 16px; border-radius: 50%; background: var(--ink); }

  .headline {
    left: 320px; top: 40px; width: 560px;
    font-weight: 700; white-space: nowrap;
  }
  .headline-line {
    display: block; font-size: 45px; line-height: 58px;
    letter-spacing: -0.3px;
  }
  .headline-big {
    display: block; font-size: 79px; line-height: 1;
    margin-top: 6px; letter-spacing: -0.5px;
  }

  .photo-slot { left: 20px; top: 322px; width: 425px; height: 583px; }

  .info { left: 477px; width: 400px; }
  .info-heading {
    font-size: 25px; font-weight: 700; color: var(--accent-blue);
    text-transform: uppercase; letter-spacing: 0.2px; line-height: 1.15;
    white-space: nowrap;
  }
  .info-body { font-size: 20.5px; line-height: 1.27; color: var(--white); white-space: nowrap; }
  .info-body strong { font-weight: 700; }

  .plans-banner { left: 465px; top: 600px; width: 300px; height: 46px; }
  .plans-title {
    left: 476px; top: 601px; font-size: 36px; font-weight: 700;
    color: var(--white); letter-spacing: 0.3px; white-space: nowrap;
  }
  .price-tag { left: 476px; top: 778px; width: 210px; height: 92px; }
  .price-amount { left: 478px; top: 805px; width: 86px; text-align: center; font-size: 32px; font-weight: 700; }
  .price-unit { left: 572px; top: 810px; font-size: 23px; color: var(--white); white-space: nowrap; }

  .contact { left: 0; width: 891px; text-align: center; white-space: nowrap; }
  .contact-title { top: 925px; font-size: 37px; font-weight: 700; }
  .contact-sub { top: 966px; font-size: 31px; font-weight: 700; letter-spacing: 0.3px; }
  .contact-rule { left: 87px; top: 1016px; width: 714px; height: 1px; background: #9a9a9a; }
  .contact-phone { top: 1028px; font-size: 41px; font-weight: 700; }
  .contact-web { top: 1071px; font-size: 22px; }
</style>
</head>
<body>
<main class="flier">
  <svg class="flier-backdrop" viewBox="0 0 891 1150" width="891" height="1150" aria-hidden="true">
    <defs>
      <radialGradient id="panelGlow" cx="0.3" cy="0.55" r="0.6">
        <stop offset="0" stop-color="#4a4a4a"/>
        <stop offset="1" stop-color="#0b0b0b"/>
      </radialGradient>
      <linearGradient id="footerShade" x1="0" y1="0" x2="0" y2="1">
        <stop offset="0" stop-color="#666666"/>
        <stop offset="1" stop-color="#575757"/>
      </linearGradient>
    </defs>
    <rect width="891" height="1150" fill="url(#panelGlow)"/>
    <polygon points="0,0 891,0 891,250 288,250 0,355" fill="var(--brand-blue)"/>
    <polyline points="0,360 290,256 891,256" fill="none" stroke="var(--white)" stroke-width="6"/>
    <polygon points="0,908 603,908 891,803 891,1150 0,1150" fill="url(#footerShade)"/>
    <polyline points="0,906 601,906 891,800" fill="none" stroke="var(--white)" stroke-width="6"/>
  </svg>

  <div class="abs brand-name"><span class="brand-dot"></span>Lantern Scholars</div>

  <h1 class="abs headline">
    <span class="headline-line">Personalized Tutoring From</span>
    <span class="headline-line">STEM Experts Via Your</span>
    <span class="headline-big">MOBILE DEVICE</span>
  </h1>

  <svg class="abs photo-slot" viewBox="0 0 425 583" role="img" aria-label="Photo of a hand holding a smartphone showing a tutoring chat with homework snapshots">
    <defs>
      <radialGradient id="photoTone" cx="0.55" cy="0.5" r="0.6">
        <stop offset="0" stop-color="#d9b6a3"/>
        <stop offset="0.7" stop-color="#8a7168"/>
        <stop offset="1" stop-color="#2a2a2a" stop-opacity="0"/>
      </radialGradient>
    </defs>
    <rect width="425" height="583" fill="url(#photoTone)"/>
  </svg>

  <section class="abs info" style="top:278px">
    <h2 class="info-heading">Subjects</h2>
    <p class="info-body">All Math, Science, Standardized Test Prep,<br>and Writing 6th-12th grade.</p>
  </section>
  <section class="abs info" style="top:373px">
    <h2 class="info-heading">Our Tutors Are Local</h2>
    <p class="info-body">St. Louis PhD candidates or<br>PhD degree holders in STEM fields.</p>
  </section>
  <section class="abs info" style="top:469px">
    <h2 class="info-heading">No Scheduling Required!</h2>
    <p class="info-body">As soon as you send a message for help,<br>a tutor will respond to set up a study session<br>as soon as possible.</p>
  </section>

  <svg class="abs plans-banner" viewBox="0 0 300 46" aria-hidden="true">
    <polygon points="0,0 268,0 300,46 0,46" fill="var(--brand-blue)"/>
  </svg>
  <h2 class="abs plans-title">PAYMENT PLANS</h2>

  <section class="abs info" style="top:654px">
    <h3 class="info-heading">Pay-As-You-Go</h3>
    <p class="info-body"><strong>$0.83</strong>/ minute. <strong>$0</strong> up-front<br>before session begins!</p>
  </section>
  <section class="abs info" style="top:750px">
    <h3 class="info-heading">Unlimited Subscription</h3>
  </section>

  <svg class="abs price-tag" viewBox="0 0 210 92" aria-hidden="true">
    <polygon points="50,17 185,17 205,47 185,77 50,77" fill="var(--deep-blue)" stroke="#8fb8e0" stroke-width="1.5"/>
    <circle cx="45" cy="47" r="43" fill="var(--brand-blue)" stroke="#1e4f82" stroke-width="2"/>
  </svg>
  <div class="abs price-amount">$150</div>
  <div class="abs price-unit">Per Month</div>

  <p class="abs contact contact-title">CONTACT US TODAY</p>
  <p class="abs contact contact-sub">TO SET UP FOR YOUR FIRST, FREE TUTORING SESSION</p>
  <div class="abs contact-rule"></div>
  <p class="abs contact contact-phone">Phone : 866-555-0142</p>
  <p class="abs contact contact-web">www.lanternscholars.com &nbsp;|&nbsp; tutor@lanternscholars.com</p>
</main>
</body>
</html>
```